Update of unique sports email website.

Hello.
I would like you to update a ol' archived website of mine. Bring it back to life with updated html5 or wordpress with plugins. I will provide the wordpress plugins by downloading from wordpress.org. It has 5-6 pages. Will need to update some stock sports photos.
It will be hosted on a vps server with linux and fantastico and softicious installed.
The website caters to the middle, junior, and high schools in america that has a mascot for their sports teams. The website will provide vanity email addresses that will be forwarded to their home/work/school email account. We will need a form that confirms valid email information on a form, send a confirmation page to the new clients email address that is given , they click that to confirm their enrollment. A paypal link to be installed.
I can and will provide the previous attempts of this website for any guidance and reflection to the new updated version. Other websites that are similar, or we like the design or copy : www.Brivatpost.com for frontpage colors and whitespace.
Target Market(s)
this updated website will have clicks from all over the world. the paying customer will be from mostly the united states. Sports audience. Middle schoolers, high schoolers, parents, coaches, teachers, students, administrators who all want a highly desirable sports email address of their favorite team, or local high school .
Kalvix Marketing has identified and acquired the most popular sports mascots in America's most popular high school sports. We want to offer these two-worded domains to the sports amateur market. No professional teams. Strictly high schools and young adults.
Industry/Entity Type
School
Requirements
Must have
- easy to read, easy to look at, easy on the eyes. Lots of white space. A few colors . Standard black text/fonts.
A paypal.com link to accept immediate payments. Then a confirmation email sent to him and us(kalvix, inc) indicating the quick payment and start processing his email request by hand. A human will always look/check/verify the email address request.
Professional look. Classy look. Fast loading.
html5 complied.
Somekind of interesting header.
Need to handle the sports: Baseball, basketball, lacrosse(lax), football, volleyball, softball, track, and soccer.
Should not have
- sloppy text and pages.
ugly colors and combinations.
Lots of questions.

```html
<!DOCTYPE html>
<html lang="en">
<head>
<meta charset="utf-8">
<title>MyTeamPost.com</title>
<link href="https://fonts.googleapis.com/css2?family=Arimo:wght@400;700&display=swap" rel="stylesheet">
<style>
:root{
  --brand:#e5432a;
  --brand-dark:#c92f18;
  --ink:#000;
  --muted:#9a9a9a;
  --field:#c8c8c8;
  --bg:#fff;
  --photo-a:#c9742f;
  --photo-b:#e8e2da;
}
*{box-sizing:border-box;margin:0;padding:0}
html,body{width:1200px;height:922px;overflow:hidden;background:var(--bg);font-family:"Arimo",Arial,sans-serif;color:var(--ink)}
.page{position:relative;width:1200px;height:922px}
.brand{position:absolute;left:42px;top:34px;font-size:38px;font-weight:400;color:var(--brand);letter-spacing:.2px}
.tabs{position:absolute;left:424px;top:91px;display:flex;gap:4px;list-style:none}
.tabs li{height:37px;border-radius:6px 6px 0 0;background:linear-gradient(#f0563c,var(--brand-dark));color:#fff;font-size:17px;display:flex;align-items:center;justify-content:center;border:2px solid var(--brand)}
.tabs li.active{background:#fff;color:var(--brand);border-bottom-color:#fff;height:40px;position:relative;z-index:2}
.main{position:absolute;left:36px;top:127px;width:1137px;height:662px;border:2px solid var(--brand);border-radius:12px;overflow:hidden;background:#fff}
.hero-photo{position:absolute;left:0;top:60px;width:700px;height:600px;background:radial-gradient(ellipse at 40% 70%,var(--photo-a) 0%,#b8552a 35%,var(--photo-b) 75%,#fff 100%)}
.welcome{position:absolute;left:488px;top:40px;width:640px}
.welcome h1{font-size:35px;font-weight:700;margin-bottom:24px}
.welcome p{font-size:16px;font-weight:700;line-height:23px;letter-spacing:.4px;margin-bottom:23px}
.welcome a{color:var(--brand);text-decoration:underline}
.login{position:absolute;left:688px;top:443px;width:428px;height:192px;border:3px solid #a8a8a8;border-radius:14px;background:rgba(255,255,255,.88);font-size:15px}
.login label{position:absolute;left:17px}
.login .field{position:absolute;left:112px;width:296px;height:40px;border:2px solid var(--field);border-radius:6px;background:#fff}
.login .signup{position:absolute;left:17px;top:150px}
.login .register{position:absolute;left:198px;top:150px;color:var(--brand);text-decoration:underline}
.login .btn{position:absolute;left:305px;top:130px;width:104px;height:40px;border-radius:6px;background:linear-gradient(#f5623f,var(--brand-dark));color:#fff;font-size:18px;display:flex;align-items:center;justify-content:center}
.footer-nav{position:absolute;top:812px;left:0;width:1200px;display:flex;justify-content:center;font-size:15px;font-weight:700;letter-spacing:.4px}
.footer-nav span.sep{margin:0 17px;font-weight:400}
.legal{position:absolute;top:845px;left:0;width:1200px;text-align:center;font-size:13px}
</style>
</head>
<body>
<div class="page">
  <div class="brand">myteampost.com</div>
  <ul class="tabs">
    <li class="active" style="width:78px">Home</li>
    <li style="width:105px">About Us</li>
    <li style="width:100px">Mascots</li>
    <li style="width:136px">Merchandise</li>
    <li style="width:70px">FAQ</li>
    <li style="width:110px">Investors</li>
    <li style="width:111px">Contact Us</li>
  </ul>
  <main class="main">
    <div class="hero-photo" role="img" aria-label="Collection of sports equipment: basketball, football, baseball glove, catcher's mask, boxing gloves, tennis ball, golf ball, hockey puck and rackets"></div>
    <section class="welcome">
      <h1>Welcome to MyTeamPost.com</h1>
      <p>The Internet's Largest Purveyor of High Schools, Colleges, and Universities Nicknames and Team Mascots for Email and Team Websites.</p>
      <p>View our Serious <a href="#">Collection</a> of America's Most Famous Nicknames and Team Mascots. Each Will Be Available For All Your Team Email Needs.</p>
    </section>
    <form class="login">
      <label style="top:30px">Username</label><div class="field" style="top:18px"></div>
      <label style="top:83px">Password</label><div class="field" style="top:71px"></div>
      <span class="signup">Don't have an account?</span>
      <a class="register" href="#">Register now!</a>
      <span class="btn">LOGIN</span>
    </form>
  </main>
  <nav class="footer-nav">
    <span>Home</span><span class="sep">|</span><span>Mascots</span><span class="sep">|</span><span>About Us</span><span class="sep">|</span><span>Merchandise</span><span class="sep">|</span><span>FAQ</span><span class="sep">|</span><span>Investors</span><span class="sep">|</span><span>Contact Us</span>
  </nav>
  <p class="legal">This Sports Mail Service Is Not Sponsored or Owned by Any professional , collegiate, or high school organization. A Kalvix Marketing venture.</p>
</div>
</body>
</html>
```